Crestline Lending Group Business Cards

We are looking to revamp the current business cards each of our locations uses. We are a lending company that specializes in personal loans, title loans, and tax services. We have locations in New Mexico, Texas, and Oklahoma.

We would like a cleaner, sleeker look while still highlighting what we offer. Title Loans, Personal Loans & Tax Services. We also want to include our referral fee somewhere on the card. We would like to see an English option as well as a Spanish option for the cards.

PLEASE NOTE: Some business cards do not include the employee's name but just the store's location, while others will include both.

These are double-sided business cards, and we would like to see proof if possible. I have included proofs of our current business cards for you to review below, as well as our company logo. Feel free to get creative with the logo, etc! Colors should match the logo; however, you do not need to use all of our logo colors if you don't want to.

```html
<!DOCTYPE html>
<html lang="en">
<head>
<meta charset="utf-8">
<title>Crestline Lending Group — Business Card</title>
<link href="https://fonts.googleapis.com/css2?family=Anton&family=Montserrat:ital,wght@0,400;0,600;0,700;0,800;1,800&display=swap" rel="stylesheet">
<style>
  :root{
    --green:#2f6043;
    --red:#c2202a;
    --ink:#231f20;
    --text:#3b3b3b;
    --white:#ffffff;
    --backdrop:#e2e2e6;
    --line:#4a4a4a;
  }
  *{margin:0;padding:0;box-sizing:border-box}
  html,body{width:1200px;height:1200px;overflow:hidden;background:var(--backdrop);font-family:"Montserrat",sans-serif}
  .canvas{position:relative;width:1200px;height:1200px}
  .card{position:absolute;left:218px;width:764px;height:440px;border-radius:44px;overflow:hidden;background:var(--white)}
  .card--front{top:104px}
  .card--back{top:648px}

  /* front */
  .brand-name,.brand-web{position:absolute;writing-mode:vertical-rl;transform:rotate(180deg);text-align:center;white-space:nowrap}
  .brand-name{left:148px;top:40px;height:360px;color:var(--green);font-weight:700;font-size:34px;line-height:1.08}
  .brand-web{left:234px;top:34px;height:250px;color:var(--red);font-weight:600;font-size:15px;letter-spacing:.3px;line-height:1.2}
  .divider{position:absolute;left:313px;top:60px;width:6px;height:330px;background:linear-gradient(to right,rgba(0,0,0,.08),rgba(0,0,0,0));filter:blur(2px)}
  .person{position:absolute;left:344px;top:64px}
  .person__name{font-size:45px;font-weight:800;line-height:1;color:var(--green)}
  .person__name .first{color:var(--red)}
  .person__role{font-size:20px;color:var(--red);margin-top:2px}
  .contact-rail{position:absolute;left:355px;top:190px;width:4px;height:150px;background:var(--line)}
  .contact{position:absolute;left:348px;display:flex;align-items:center}
  .contact__icon{width:47px;height:47px;border-radius:7px;display:flex;align-items:center;justify-content:center;flex:none}
  .contact__icon--red{background:var(--red)}
  .contact__icon--green{background:var(--green)}
  .contact__text{margin-left:21px;color:var(--text)}
  .contact--phone{top:167px}
  .contact--phone .contact__text{font-size:24px;font-weight:700}
  .contact--mail{top:244px}
  .contact--mail .contact__text{font-size:21px;font-weight:400;letter-spacing:.3px}
  .contact--place{top:316px}
  .contact--place .contact__text{font-size:20px;font-weight:700;line-height:1.3;margin-top:-16px}

  /* back */
  .back-art{position:absolute;inset:0}
  .offer{position:absolute;left:52px;top:65px;width:288px;height:288px;text-align:center}
  .offer__lead{position:absolute;left:0;right:0;top:70px;font-size:39px;font-weight:800;color:var(--ink)}
  .offer__amount{position:absolute;left:0;right:0;top:110px;font-family:"Anton",sans-serif;font-size:104px;line-height:1;color:var(--ink)}
  .refer{position:absolute;left:348px;top:121px;width:391px;height:61px;background:var(--white);display:flex;align-items:center;justify-content:center}
  .refer__text{color:var(--red);font-weight:800;font-style:italic;font-size:45px}
  .services{position:absolute;left:388px;top:218px;list-style:none}
  .services li{display:flex;align-items:center;height:39px;color:var(--white);font-weight:700;font-size:32px}
  .services svg{width:34px;height:32px;margin-right:10px;flex:none}
</style>
</head>
<body>
<main class="canvas">

  <section class="card card--front" aria-label="Card front">
    <div class="brand-name">Crestline<br>Lending Group</div>
    <div class="brand-web">www.crestlinelending.com</div>
    <div class="divider"></div>

    <div class="person">
      <h1 class="person__name"><span class="first">Marcus</span> Delgado</h1>
      <p class="person__role">Branch Manager</p>
    </div>

    <div class="contact-rail"></div>
    <div class="contact contact--phone">
      <span class="contact__icon contact__icon--red">
        <svg width="22" height="22" viewBox="0 0 24 24"><path fill="#fff" d="M6.6 10.8a15.1 15.1 0 0 0 6.6 6.6l2.2-2.2c.3-.3.7-.4 1-.2 1.1.4 2.3.6 3.6.6.6 0 1 .4 1 1V20c0 .6-.4 1-1 1A17 17 0 0 1 3 4c0-.6.4-1 1-1h3.5c.6 0 1 .4 1 1 0 1.3.2 2.5.6 3.6.1.3 0 .7-.2 1z"/></svg>
      </span>
      <span class="contact__text">(505) 555-0148</span>
    </div>
    <div class="contact contact--mail">
      <span class="contact__icon contact__icon--green">
        <svg width="24" height="24" viewBox="0 0 24 24" fill="none" stroke="#fff" stroke-width="1.8"><circle cx="12" cy="12" r="9"/><path d="M3 12h18M12 3c3 3 3 15 0 18M12 3c-3 3-3 15 0 18"/></svg>
      </span>
      <span class="contact__text">hello@crestlinelending.com</span>
    </div>
    <div class="contact contact--place">
      <span class="contact__icon contact__icon--red">
        <svg width="20" height="24" viewBox="0 0 20 24"><path fill="#fff" d="M10 1a8 8 0 0 0-8 8c0 6 8 14 8 14s8-8 8-14a8 8 0 0 0-8-8zm0 11a3 3 0 1 1 0-6 3 3 0 0 1 0 6z"/></svg>
      </span>
      <span class="contact__text">450 Mesa Avenue, Suite B,<br>Riverton, Texas 75001</span>
    </div>
  </section>

  <section class="card card--back" aria-label="Card back">
    <svg class="back-art" width="764" height="440" viewBox="0 0 764 440">
      <rect width="764" height="440" fill="#ffffff"/>
      <path d="M0 0H252C200 60 122 220 170 440H0Z" fill="var(--green)"/>
      <path d="M284 0H764V440H198C160 220 228 62 284 0Z" fill="var(--red)"/>
      <circle cx="196" cy="209" r="144" fill="#ffffff"/>
    </svg>

    <div class="offer">
      <p class="offer__lead">Get upto</p>
      <p class="offer__amount">$100</p>
    </div>

    <div class="refer"><span class="refer__text">Refer a Friend</span></div>

    <ul class="services">
      <li><svg viewBox="0 0 34 32"><path d="M2 17l10 11L32 3" fill="none" stroke="#fff" stroke-width="6" stroke-linejoin="round"/></svg>Title Loans</li>
      <li><svg viewBox="0 0 34 32"><path d="M2 17l10 11L32 3" fill="none" stroke="#fff" stroke-width="6" stroke-linejoin="round"/></svg>Personal Loans</li>
      <li><svg viewBox="0 0 34 32"><path d="M2 17l10 11L32 3" fill="none" stroke="#fff" stroke-width="6" stroke-linejoin="round"/></svg>Tax Services</li>
    </ul>
  </section>

</main>
</body>
</html>
```